Laundromat Grand Opening.

Laundromat /Grand opening. One side English, one side Spanish. Include the Address, Name, Raffle/Prizes and Grand opening date.
Ridgeview Suds Laundromat, 418 W. Harlan Ave. 2/7/2016. (555) 314-2297.

Industry/Entity Type

Coin

Colors
000000

Requirements
Nice to have
• Eye catching. Laundry theme.

```html
<!DOCTYPE html>
<html lang="en">
<head>
<meta charset="utf-8">
<title>Ridgeview Suds Laundromat – Grand Opening Flyers</title>
<link href="https://fonts.googleapis.com/css2?family=Great+Vibes&family=Roboto:wght@400;700&family=Roboto+Condensed:wght@400&display=swap" rel="stylesheet">
<style>
  :root {
    --page: #e9e7e4;
    --ink: #000000;
    --white: #ffffff;
    --silver: #d6d6d6;
    --grey-text: #bdbdbd;
    --photo-light: #e4e4e6;
    --photo-dark: #8d8d90;
    --tag-ink: #1a1a1a;
    --tag-note: #555555;
  }
  * { box-sizing: border-box; margin: 0; padding: 0; }
  html, body { width: 1200px; height: 903px; overflow: hidden; background: var(--page); }
  body { position: relative; font-family: "Roboto", Arial, sans-serif; }

  .flyer {
    position: absolute;
    top: 84px;
    width: 492px;
    height: 723px;
    background: var(--ink);
    box-shadow: 0 4px 14px rgba(0,0,0,0.35);
    overflow: hidden;
  }
  .flyer--english { left: 68px; }
  .flyer--spanish { left: 636px; }

  .flyer__header { position: absolute; top: 0; left: 0; right: 0; height: 144px; text-align: center; }
  .flyer__business {
    position: absolute; top: 23px; left: 0; right: 0;
    color: var(--white); font-size: 22px; letter-spacing: 1px; text-transform: uppercase;
    white-space: nowrap;
  }
  .flyer__headline {
    position: absolute; top: 62px; left: 0; right: 0;
    font-family: "Great Vibes", cursive; font-weight: 400; font-size: 62px; line-height: 1;
    letter-spacing: 1px; word-spacing: 6px;
    color: var(--silver); white-space: nowrap;
  }

  .flyer__photo {
    position: absolute; top: 144px; left: 0; right: 0; height: 379px;
    background: linear-gradient(135deg, var(--photo-light) 0%, var(--photo-dark) 100%);
  }

  .flyer__tag { position: absolute; top: 394px; left: 310px; width: 162px; height: 93px; }
  .flyer__tag-label {
    position: absolute; left: 4px; right: 4px; top: 33px;
    text-align: center; font-family: "Roboto Condensed", Arial, sans-serif;
    font-size: 25px; line-height: 1; color: var(--tag-ink); white-space: nowrap;
  }
  .flyer__tag-note {
    position: absolute; left: 4px; right: 4px; top: 66px;
    text-align: center; font-size: 10px; line-height: 1; color: var(--tag-note); white-space: nowrap;
  }

  .flyer__date {
    position: absolute; top: 558px; left: 0; right: 0; text-align: center;
    color: var(--white); font-weight: 700; font-size: 30px; letter-spacing: 0.5px;
    white-space: nowrap;
  }
  .flyer__rule {
    position: absolute; top: 602px; left: 134px; width: 259px;
    border-top: 2px dotted var(--grey-text);
  }
  .flyer__time {
    position: absolute; top: 612px; left: 0; right: 0; text-align: center;
    color: var(--white); font-size: 20px; white-space: nowrap;
  }
  .flyer__contact {
    position: absolute; top: 676px; left: 0; right: 0; text-align: center;
    color: var(--grey-text); font-size: 14px; white-space: nowrap;
  }
</style>
</head>
<body>

<section class="flyer flyer--english" lang="en">
  <header class="flyer__header">
    <p class="flyer__business">Ridgeview Suds Laundry</p>
    <h1 class="flyer__headline">Grand Opening</h1>
  </header>
  <div class="flyer__photo" role="img" aria-label="Photo of a front-loading washing machine door with colourful clothes tumbling inside"></div>
  <div class="flyer__tag">
    <svg width="162" height="93" viewBox="0 0 162 93" aria-hidden="true">
      <defs>
        <linearGradient id="tagFillEn" x1="0" y1="0" x2="0" y2="1">
          <stop offset="0" stop-color="#f6f6f6"/><stop offset="1" stop-color="#b8b8b8"/>
        </linearGradient>
      </defs>
      <path d="M8 18 H20 L30 2 L34 18 H154 Q160 18 160 24 V85 Q160 91 154 91 H8 Q2 91 2 85 V24 Q2 18 8 18 Z" fill="url(#tagFillEn)" stroke="#888" stroke-width="1"/>
      <rect x="7" y="23" width="148" height="63" rx="4" fill="none" stroke="#777" stroke-dasharray="3 2"/>
      <g fill="none" stroke="#444" stroke-width="1">
        <path d="M56 26 h10 l-2 7 h-6 z"/><path d="M72 26 l5 7 l5-7 z"/><rect x="87" y="26" width="7" height="7"/><path d="M99 27 h8 l-4 6 z"/>
      </g>
    </svg>
    <p class="flyer__tag-label">Raffle/Prizes</p>
    <p class="flyer__tag-note">Ridgeview Suds Laundromat</p>
  </div>
  <p class="flyer__date">FEB 7TH. 2016</p>
  <div class="flyer__rule"></div>
  <p class="flyer__time">Time 7:00 a.m till 10:00p.m</p>
  <p class="flyer__contact">418 W. Harlan Ave. Ridgeview, CA 90210 &nbsp;|&nbsp; (555) 314-2297</p>
</section>

<section class="flyer flyer--spanish" lang="es">
  <header class="flyer__header">
    <p class="flyer__business">Lavandería Ridgeview Suds</p>
    <h1 class="flyer__headline">Gran Inauguración</h1>
  </header>
  <div class="flyer__photo" role="img" aria-label="Foto de la puerta de una lavadora con ropa de colores girando dentro"></div>
  <div class="flyer__tag">
    <svg width="162" height="93" viewBox="0 0 162 93" aria-hidden="true">
      <defs>
        <linearGradient id="tagFillEs" x1="0" y1="0" x2="0" y2="1">
          <stop offset="0" stop-color="#f6f6f6"/><stop offset="1" stop-color="#b8b8b8"/>
        </linearGradient>
      </defs>
      <path d="M8 18 H20 L30 2 L34 18 H154 Q160 18 160 24 V85 Q160 91 154 91 H8 Q2 91 2 85 V24 Q2 18 8 18 Z" fill="url(#tagFillEs)" stroke="#888" stroke-width="1"/>
      <rect x="7" y="23" width="148" height="63" rx="4" fill="none" stroke="#777" stroke-dasharray="3 2"/>
      <g fill="none" stroke="#444" stroke-width="1">
        <path d="M56 26 h10 l-2 7 h-6 z"/><path d="M72 26 l5 7 l5-7 z"/><rect x="87" y="26" width="7" height="7"/><path d="M99 27 h8 l-4 6 z"/>
      </g>
    </svg>
    <p class="flyer__tag-label">Rifa/Premios</p>
    <p class="flyer__tag-note">Ridgeview Suds Laundromat</p>
  </div>
  <p class="flyer__date">FEBRERO 7º. 2016</p>
  <div class="flyer__rule"></div>
  <p class="flyer__time">7:00 am hasta las 10:00 pm</p>
  <p class="flyer__contact">418 W. Harlan Ave. Ridgeview, CA 90210 &nbsp;|&nbsp; (555) 314-2297</p>
</section>

</body>
</html>
```